Electrical Contracting Business Website

Require website done for my contracting business.
Partly done one but really dont have time.

You can view the current one at http://tolbran.net.au

You can use any info/styles/photos from the current website

I like the orange color of the logo so id like things to be with that
Unfortunatly being a new business (Sept 2015) I havent got alot of photos . but if you require any for any of the specifics listed in the doc file ill have a look to see what I have.

I am targeting mainly commercial / industrial clients. Which also includes government and mining.

Target Market(s)

People requiring electricians

Industry/Entity Type

Electrician

Coding

Coded - Design and coding required

Number of Pages Required

5+ page

Colors
f37122

Requirements
Must have
• logo with EC Number
• Keep it simple and not to complicated
• Comply with the current html / style sheet standards.
• Desktop/Mobile Version compatability
Nice to have
• additional photos.
• The domestic lifts we install are by vonrim I dont have any photos of them unfortunately.
Should not have
• change colour of logo

```html
<!DOCTYPE html>
<html lang="en">
<head>
<meta charset="utf-8">
<title>Tolbran Engineering</title>
<link href="https://fonts.googleapis.com/css2?family=Open+Sans:wght@400;600;700;800&display=swap" rel="stylesheet">
<style>
:root{
  --orange:#f37122;
  --dark:#3d4043;
  --light:#e9e9e9;
  --text:#333;
  --muted:#666;
  --white:#fff;
}
*{box-sizing:border-box;margin:0;padding:0}
html,body{width:1200px;height:3068px;overflow:hidden;background:var(--white);font-family:'Open Sans',Arial,sans-serif;color:var(--text)}
.site-header{height:120px;position:relative}
.brand{position:absolute;left:40px;top:30px;display:flex;align-items:center;gap:12px}
.brand-dot{width:44px;height:44px;border-radius:50%;background:var(--orange)}
.brand-name{font-weight:800;font-size:40px;color:var(--orange);letter-spacing:1px}
.top-contacts{position:absolute;right:24px;top:10px;display:flex;gap:40px;font-size:13px;color:var(--muted)}
.top-contacts span{display:flex;align-items:center;gap:8px}
.top-contacts i{width:14px;height:14px;border-radius:50%;background:var(--orange);display:inline-block}
.main-nav{position:absolute;right:24px;top:52px;display:flex;gap:4px}
.main-nav a{font-size:16px;font-weight:600;color:var(--text);text-decoration:none;padding:6px 12px}
.main-nav a.active{background:var(--orange);color:var(--white)}
.hero{position:relative;height:500px;background:linear-gradient(120deg,#8a8f93,#c4c8cb 45%,#6b6f72);text-align:center;color:var(--white)}
.hero h1{position:absolute;left:0;right:0;top:110px;font-size:96px;font-weight:800;line-height:1;text-shadow:0 2px 8px rgba(0,0,0,.35)}
.hero h2{position:absolute;left:0;right:0;top:205px;font-size:64px;font-weight:700;text-shadow:0 2px 8px rgba(0,0,0,.35)}
.btn{display:inline-block;background:var(--orange);color:var(--white);font-weight:600;font-size:18px;padding:14px 28px;text-decoration:none}
.hero .btn{position:absolute;left:492px;top:300px}
.welcome{height:400px;padding:44px 180px 0;text-align:center}
.welcome h2{font-size:40px;font-weight:600;color:var(--text)}
.welcome h2 span{color:var(--orange)}
.welcome-cols{display:flex;gap:100px;margin-top:30px;text-align:left}
.welcome-cols p{flex:1;font-size:16px;line-height:1.45;color:var(--text)}
.what-we-do{background:var(--dark);height:230px;color:var(--white);text-align:center;padding-top:18px}
.what-we-do h2{font-size:36px;font-weight:600;line-height:48px}
.wwd-list{display:flex;justify-content:center;gap:190px;margin-top:14px}
.wwd-item{width:140px}
.wwd-icon{width:80px;height:80px;border-radius:50%;background:var(--orange);margin:0 auto 10px;display:flex;align-items:center;justify-content:center}
.wwd-item p{font-size:19px;line-height:1.3}
.section-title{display:flex;align-items:center;justify-content:center;gap:22px;font-size:38px;font-weight:600;line-height:52px}
.section-title::before,.section-title::after{content:"";width:60px;height:2px;background:var(--text)}
.projects{padding-top:44px;height:590px}
.projects .section-title{color:var(--orange)}
.filters{display:flex;justify-content:center;gap:14px;margin-top:16px}
.filters span{border:1px solid #999;padding:2px 10px;font-size:17px;background:var(--white)}
.filters span.active{background:var(--orange);border-color:var(--orange);color:var(--white)}
.project-grid{display:grid;grid-template-columns:repeat(3,240px);gap:60px;row-gap:30px;justify-content:center;margin-top:30px}
.project{height:180px;position:relative}
.project-label{position:absolute;left:0;right:0;bottom:46px;color:var(--white);font-size:16px;text-align:center}
.specialized{background:var(--light);height:560px;padding-top:40px}
.specialized .section-title{color:var(--text)}
.specialized .section-title em{font-style:normal;color:var(--orange)}
.cards{display:flex;justify-content:center;gap:80px;margin-top:30px}
.card{width:400px;height:430px;background:var(--white);border:2px solid var(--orange);border-radius:6px;padding:14px 40px}
.card-icon{display:flex;justify-content:center}
.card h3{text-align:center;font-size:24px;font-weight:600;margin:6px 0 10px}
.card ul{list-style:none}
.card li{font-size:15px;line-height:23px;padding-left:20px;position:relative}
.card li::before{content:"";position:absolute;left:2px;top:9px;width:6px;height:6px;background:var(--orange)}
.contact{background:var(--orange);height:600px;position:relative;color:var(--white)}
.contact .section-title{padding-top:44px;color:var(--white);font-weight:400}
.contact .section-title::before,.contact .section-title::after{background:var(--white)}
.contact-form{position:absolute;left:140px;top:150px;width:560px}
.field{background:var(--white);color:var(--text);font-size:18px;padding:0 16px;height:48px;line-height:48px;margin-bottom:20px;border-radius:3px}
.field.message{height:128px;line-height:1.6;padding-top:8px}
.submit{display:block;width:170px;margin:24px auto 0;border:1px solid var(--white);text-align:center;padding:6px;font-size:18px}
.contact-info{position:absolute;left:800px;top:150px;font-size:15px}
.contact-info p{display:flex;align-items:center;gap:12px;margin-bottom:20px}
.contact-info i{width:22px;height:22px;border-radius:50%;background:var(--white);display:inline-block}
.contact-brand{display:flex;align-items:center;gap:12px;margin-top:30px}
.contact-brand .brand-dot{background:var(--white)}
.contact-brand .brand-name{color:var(--white)}
.site-footer{background:var(--dark);height:68px;color:#ccc;font-size:13px;display:flex;align-items:center;justify-content:space-between;padding:0 40px}
.social{display:flex;align-items:center;gap:12px}
.social i{width:28px;height:28px;border-radius:50%;background:var(--orange);display:inline-block}
</style>
</head>
<body>
<header class="site-header">
  <div class="brand"><span class="brand-dot"></span><span class="brand-name">TOLBRAN</span></div>
  <div class="top-contacts">
    <span><i></i>+61 0400 118 726</span>
    <span><i></i>+61 (08) 6100 4420</span>
    <span><i></i>info@tolbran.net.au</span>
  </div>
  <nav class="main-nav">
    <a class="active" href="#">HOME</a><a href="#">ABOUT US</a><a href="#">RESIDENTIAL</a><a href="#">COMMERCIAL</a><a href="#">INDUSTRIAL</a><a href="#">CONTACT US</a>
  </nav>
</header>

<section class="hero" role="img" aria-label="Electrician working on a commercial switchboard">
  <h1>COMMERCIAL</h1>
  <h2>SERVICE</h2>
  <a class="btn" href="#">KNOW MORE</a>
</section>

<section class="welcome">
  <h2>Welcome to <span>TOLBRAN Engineering</span></h2>
  <div class="welcome-cols">
    <p>The main body should clearly state the points that you want to make. As a general rule it is good idea to keep this as to the point as possible to ensure that the recipient remains engaged. A longer main body may be more appropriate when making a complaint as you may require to add more detail in order to convey.</p>
    <p>The main body should clearly state the points that you want to make. As a general rule it is good idea to keep this as to the point as possible to ensure that the recipient remains engaged.</p>
  </div>
</section>

<section class="what-we-do">
  <h2>What We DO ?</h2>
  <div class="wwd-list">
    <div class="wwd-item"><div class="wwd-icon"><svg width="44" height="44" viewBox="0 0 48 48"><path d="M6 24 24 8l18 16h-6v16H12V24z" fill="#fff"/><rect x="20" y="28" width="8" height="12" fill="#f37122"/></svg></div><p>Residential<br>Services</p></div>
    <div class="wwd-item"><div class="wwd-icon"><svg width="44" height="44" viewBox="0 0 48 48"><rect x="12" y="6" width="24" height="36" fill="#fff"/><g fill="#f37122"><rect x="16" y="11" width="5" height="5"/><rect x="27" y="11" width="5" height="5"/><rect x="16" y="20" width="5" height="5"/><rect x="27" y="20" width="5" height="5"/><rect x="16" y="29" width="5" height="5"/><rect x="27" y="29" width="5" height="5"/></g></svg></div><p>Commercial<br>Services</p></div>
    <div class="wwd-item"><div class="wwd-icon"><svg width="44" height="44" viewBox="0 0 48 48"><path d="M6 42V22l10 6v-6l10 6v-6l10 6V8h6v34z" fill="#fff"/></svg></div><p>Industrial<br>Services</p></div>
  </div>
</section>

<section class="projects">
  <h2 class="section-title">Recent Project</h2>
  <div class="filters"><span class="active">All</span><span>Residential</span><span>Commercial</span><span>Industrial</span></div>
  <div class="project-grid">
    <div class="project" role="img" aria-label="Residential electrical work" style="background:linear-gradient(#5b6066,#2d2f33)"><span class="project-label">Residential Work</span></div>
    <div class="project" role="img" aria-label="Commercial lighting installation" style="background:linear-gradient(135deg,#c47a3a,#4a3424)"></div>
    <div class="project" role="img" aria-label="Industrial factory floor" style="background:linear-gradient(#d7e3ea,#8fb2c4)"></div>
    <div class="project" role="img" aria-label="Switchboard wiring" style="background:linear-gradient(135deg,#9aa3a8,#3e4a52)"></div>
    <div class="project" role="img" aria-label="Electrical cabinet room" style="background:linear-gradient(#b8b8b4,#6e6e6a)"></div>
    <div class="project" role="img" aria-label="Clean room ceiling lighting" style="background:linear-gradient(#f0f2f4,#b8c0c6)"></div>
  </div>
</section>

<section class="specialized">
  <h2 class="section-title"><span>We Specialized <em>Electrical</em> Services</span></h2>
  <div class="cards">
    <div class="card">
      <div class="card-icon"><svg width="46" height="46" viewBox="0 0 46 46"><path d="M10 36 30 16M16 36 36 16" stroke="#f37122" stroke-width="5" stroke-linecap="round"/><circle cx="34" cy="12" r="7" fill="none" stroke="#f37122" stroke-width="4"/></svg></div>
      <h3>Services</h3>
      <ul>
        <li>Automation and Control</li><li>Construction and Maintenance</li><li>Dust Collectors</li><li>Food Processing &amp; Packaging</li><li>Gantry / Jib Cranes</li><li>Generators</li><li>Man &amp; Material Hoists</li><li>Motors &amp; Pumps</li><li>Tower Cranes</li><li>Transformers</li><li>Variable Speed Drives</li><li>Radio Control</li>
      </ul>
    </div>
    <div class="card">
      <div class="card-icon"><svg width="46" height="46" viewBox="0 0 46 46"><circle cx="23" cy="18" r="11" fill="#f37122"/><rect x="18" y="30" width="10" height="8" fill="#f37122"/><path d="M23 2v3M7 18H4M42 18h-3M11 6l2 2M35 6l-2 2" stroke="#f37122" stroke-width="3"/></svg></div>
      <h3>General Services</h3>
      <ul>
        <li>Electrical Installations</li><li>Voice, and Data Cabling</li><li>Electrical Modifications</li><li>Fault Finding</li><li>Panel Upgrades</li><li>Security Lighting</li><li>Generator Hookup</li><li>Surge Protection</li><li>Building Maintenance</li><li>Lift Maintenance</li><li>Crane/Hoist Maintenance</li><li>Labour Hire</li>
      </ul>
    </div>
  </div>
</section>

<section class="contact">
  <h2 class="section-title">Contact Us</h2>
  <div class="contact-form">
    <div class="field">Name</div>
    <div class="field">E-mail</div>
    <div class="field message">Massage</div>
    <span class="submit">SUBMIT</span>
  </div>
  <div class="contact-info">
    <p><i></i>Kelmford, Western Australia, 6099</p>
    <p><i></i>+61 0400 118 726</p>
    <p><i></i>+61 (08) 6100 4420</p>
    <p><i></i>info@tolbran.net.au</p>
    <div class="contact-brand"><span class="brand-dot"></span><span class="brand-name">TOLBRAN</span></div>
  </div>
</section>

<footer class="site-footer">
  <span>Copyright © 2016 Tolbran Engineering Pty Ltd All Rights Reserved EC 12000</span>
  <div class="social"><span>Follow Us :</span><i></i><i></i><i></i><i></i></div>
</footer>
</body>
</html>
```